IT Consulting Business Card Design

We need a business card on our company name....which is a IT consulting and staffing company. We also train masters graduates in various IT courses. 70% of the time these cards will be handed out to the graduate students at the universities. 30% for our clients and business partners. We are uploading our company logo...would like to see something that matches our logo or blends with it. Please visit www.brightvaleworks.com for more details on logo and colors.

Target Market(s)

70% of the time these cards will be handed out to the graduate students at the universities. 30% for our clients and business partners.

Industry/Entity Type

Business

Contact Information for Business Card

Ravi Kondamuri
Vice-President
Bright Vale Works Inc
3807 Morrow Lane, Suite 412
East Brookridge, NJ 07315
ravi@brightvaleworks.com
Office : 1-866-219-3840 X 515
Cell number : 732-581-9034

Requirements
Nice to have
• may be company logo and name on the back of the card and detials on the other side...just a thought..!!

```html
<!DOCTYPE html>
<html lang="en">
<head>
<meta charset="utf-8">
<title>Bright Vale Works – Business Card</title>
<link href="https://fonts.googleapis.com/css2?family=Roboto:wght@400;500;700&display=swap" rel="stylesheet">
<style>
  :root {
    --page-bg: #6b3e24;
    --card-frost: rgba(255, 255, 255, 0.2);
    --card-edge: rgba(255, 255, 255, 0.45);
    --brand-red: #e0262b;
    --text-light: #ffffff;
  }
  * { box-sizing: border-box; margin: 0; padding: 0; }
  html, body {
    width: 1200px;
    height: 800px;
    overflow: hidden;
  }
  body {
    background: var(--page-bg);
    font-family: "Roboto", Arial, sans-serif;
    display: flex;
    align-items: center;
    justify-content: center;
  }
  .business-card {
    position: relative;
    width: 1050px;
    height: 600px;
    border-radius: 34px;
    background: var(--card-frost);
    border: 2px solid var(--card-edge);
    box-shadow: 0 18px 40px rgba(0, 0, 0, 0.3);
  }
  .brand {
    position: absolute;
    left: 70px;
    top: 58px;
    display: flex;
    align-items: center;
    gap: 26px;
  }
  .brand-mark {
    width: 120px;
    height: 120px;
    flex: none;
  }
  .brand-name {
    font-weight: 700;
    font-size: 46px;
    letter-spacing: 0.5px;
    color: var(--text-light);
    text-transform: uppercase;
  }
  .person {
    position: absolute;
    left: 150px;
    top: 228px;
  }
  .person-name {
    font-weight: 400;
    font-size: 44px;
    color: var(--brand-red);
    line-height: 1.1;
  }
  .person-title {
    font-weight: 400;
    font-size: 23px;
    color: var(--text-light);
    margin-top: 4px;
  }
  .contact {
    position: absolute;
    right: 72px;
    bottom: 56px;
    text-align: right;
    font-size: 27px;
    line-height: 36px;
    color: var(--text-light);
  }
  .contact .label,
  .contact .company {
    color: var(--brand-red);
    font-weight: 700;
  }
  .contact .label { margin-right: 6px; }
</style>
</head>
<body>
  <article class="business-card">
    <header class="brand">
      <svg class="brand-mark" viewBox="0 0 120 120" aria-hidden="true">
        <circle cx="60" cy="60" r="58" fill="var(--brand-red)"/>
      </svg>
      <span class="brand-name">Bright Vale Works</span>
    </header>

    <section class="person">
      <h1 class="person-name">Ravi Kondamuri</h1>
      <p class="person-title">Vice President</p>
    </section>

    <address class="contact" style="font-style: normal;">
      <div><span class="label">Office</span>866.219.3840 x515</div>
      <div><span class="label">Cell</span>732.581.9034</div>
      <div>ravi@brightvaleworks.com</div>
      <div class="company">Bright Vale Works Inc</div>
      <div>3807 Morrow Lane, Suite 412</div>
      <div>East Brookridge, NJ 07315</div>
    </address>
  </article>
</body>
</html>
```